Quillory Nest Business Card

I need a business card design. We are a collaborate online training company. Our colors are gray and green. Our website is QuilloryNest.com

I would like an area for a profile picture within the card

```html
<!DOCTYPE html>
<html lang="en">
<head>
<meta charset="utf-8">
<title>Quillory Nest Business Card</title>
<link rel="stylesheet" href="https://fonts.googleapis.com/css2?family=Open+Sans:wght@400;700&display=swap">
<style>
  :root {
    --slate: #2f3639;
    --green: #8cc63f;
    --ink: #1f2325;
    --text-gray: #555a5d;
    --paper: #ffffff;
    --backdrop: #e6e4e1;
    --photo-light: #d9dbdd;
    --photo-dark: #8a8d91;
    --caption-band: rgba(74, 78, 82, 0.82);
  }
  * { box-sizing: border-box; margin: 0; padding: 0; }
  html, body { width: 1200px; height: 1000px; overflow: hidden; }
  body {
    background: var(--backdrop);
    font-family: "Open Sans", Arial, sans-serif;
    position: relative;
  }
  .card {
    position: absolute;
    left: 243px;
    width: 708px;
    height: 404px;
    overflow: hidden;
  }
  .card-front { top: 84px; background: var(--slate); }
  .card-back { top: 526px; background: var(--paper); }

  .brand {
    position: absolute;
    display: flex;
    align-items: center;
    font-weight: 700;
    letter-spacing: -1px;
    white-space: nowrap;
  }
  .brand-dot { border-radius: 50%; background: var(--green); flex: none; }

  .card-front .brand {
    left: 0; right: 0; top: 148px;
    justify-content: center;
    gap: 18px;
    font-size: 56px;
    color: var(--paper);
  }
  .card-front .brand-dot { width: 58px; height: 58px; }

  .front-url {
    position: absolute;
    left: 0; right: 0; top: 349px;
    text-align: center;
    font-size: 17px;
    color: #e4e6e7;
  }
  .front-url .accent { color: var(--green); }

  .card-back .brand {
    left: 33px; top: 50px;
    gap: 12px;
    font-size: 34px;
    color: var(--ink);
  }
  .card-back .brand-dot { width: 40px; height: 40px; }

  .address {
    position: absolute;
    left: 89px; top: 171px;
    font-size: 17px;
    line-height: 21px;
    font-style: normal;
    color: var(--text-gray);
  }
  .contact-list {
    position: absolute;
    left: 89px; top: 232px;
    list-style: none;
    font-size: 17px;
    color: var(--text-gray);
  }
  .contact-list li {
    display: flex;
    align-items: center;
    gap: 6px;
    height: 25.5px;
  }
  .contact-list svg { width: 13px; height: 13px; flex: none; }

  .profile-photo {
    position: absolute;
    left: 382px; top: 34px;
    width: 326px; height: 370px;
    background: linear-gradient(180deg, var(--photo-light) 0%, var(--photo-dark) 100%);
  }
  .name-caption {
    position: absolute;
    left: 382px; top: 336px;
    width: 326px; height: 68px;
    background: var(--caption-band);
    text-align: center;
    padding-top: 12px;
  }
  .person-name {
    font-size: 17px;
    font-weight: 700;
    letter-spacing: 0.5px;
    color: var(--green);
    line-height: 22px;
  }
  .person-role {
    font-size: 16px;
    color: #ffffff;
    line-height: 22px;
  }
</style>
</head>
<body>

<section class="card card-front">
  <div class="brand">
    <span class="brand-dot"></span>
    <span class="brand-name">Quillory Nest</span>
  </div>
  <p class="front-url">www.<span class="accent">quillorynest</span>.com</p>
</section>

<section class="card card-back">
  <div class="brand">
    <span class="brand-dot"></span>
    <span class="brand-name">Quillory Nest</span>
  </div>

  <address class="address">
    480 Marlowe Ridge Ave. Suite 7<br>
    Fenwick, Arizona 85390
  </address>

  <ul class="contact-list">
    <li>
      <svg viewBox="0 0 16 16" aria-hidden="true"><path fill="#8cc63f" d="M4 1.5l2.3 3-1.4 1.6c.9 2 2.4 3.6 4.4 4.6l1.6-1.4 3 2.3-1.5 2.4c-5.5-.6-10-5.1-10.6-10.6z"/></svg>
      (555) 284-0196
    </li>
    <li>
      <svg viewBox="0 0 16 16" aria-hidden="true"><rect x="1" y="3" width="14" height="10" fill="#8cc63f"/><path d="M1.5 3.5L8 9l6.5-5.5" stroke="#fff" stroke-width="1.4" fill="none"/></svg>
      info@quillorynest.com
    </li>
    <li>
      <svg viewBox="0 0 16 16" aria-hidden="true"><g fill="none" stroke="#8cc63f" stroke-width="1.3"><circle cx="8" cy="8" r="6.5"/><ellipse cx="8" cy="8" rx="2.8" ry="6.5"/><path d="M1.5 8h13M2.5 4.8h11M2.5 11.2h11"/></g></svg>
      www.quillorynest.com
    </li>
  </ul>

  <div class="profile-photo" role="img" aria-label="Profile photo of the founder in a gray suit jacket"></div>
  <div class="name-caption">
    <p class="person-name">DORIAN FELL</p>
    <p class="person-role">Founder</p>
  </div>
</section>

</body>
</html>
```